A-Stand Directional Sign Design

Objective:
We need a professional graphic design for an A-Stand sign that will guide customers arriving in our parking lot to our office. The design should be visually clear, welcoming, and aligned with our brand identity.
REQUIREMENTS:
Two versions of the design:
- One with an arrow pointing left
- One with an arrow pointing right
(This allows us to place the A-Stand anywhere and flip the graphic as needed.)
DIMENSIONS:
- Viewable Area: 30" x 40"
BRAND ALIGNMENT:
- Colors, fonts, and overall style should match our website: www.skornabel.com
- Clean, modern, and professional look consistent with our aviation/tourism brand
CONTENT:
- Clear directional arrow (left or right depending on version)
- Text: “Office Entrance” or similar concise wording (designers may propose alternatives if they improve clarity)
READABILITY:
- Bold, high-contrast design for visibility from a distance
- Simple layout that avoids clutter
DELIVERABLES:
- Final artwork in print-ready format (PDF preferred)
- Two versions: Arrow Left and Arrow Right
DESIGN GOAL:
Ensure customers can easily find our office upon arrival, while reinforcing skorNABEL’s professional and welcoming brand image.
Target Market(s)
Tourism

```html
<!DOCTYPE html>
<html lang="en">
<head>
<meta charset="UTF-8">
<title>skorNABEL – Office Entrance A-Stand Signs</title>
<link rel="stylesheet" href="https://fonts.googleapis.com/css2?family=Poppins:wght@600;700&display=swap">
<style>
  :root {
    --backdrop: #f1f1f1;
    --sign-white: #ffffff;
    --brand-blue: #215eaa;
    --arrow-orange: #f39e1e;
  }
  html, body {
    margin: 0;
    padding: 0;
    width: 1200px;
    height: 857px;
    overflow: hidden;
    background: var(--backdrop);
  }
  .canvas {
    position: relative;
    width: 1200px;
    height: 857px;
  }
  .sign {
    position: absolute;
    top: 85px;
    width: 513px;
    height: 685px;
    display: flex;
    flex-direction: column;
  }
  .sign--left { left: 69px; }
  .sign--right { left: 617px; }
  .sign__header {
    height: 272px;
    background: var(--sign-white);
    display: flex;
    align-items: center;
    justify-content: center;
    gap: 16px;
  }
  .brand-dot {
    width: 34px;
    height: 34px;
    border-radius: 50%;
    background: var(--brand-blue);
  }
  .brand-name {
    font-family: "Poppins", sans-serif;
    font-weight: 700;
    font-size: 50px;
    color: var(--brand-blue);
    letter-spacing: 1px;
  }
  .sign__body {
    flex: 1;
    background: var(--brand-blue);
    position: relative;
  }
  .sign__label {
    margin: 0;
    padding-top: 44px;
    font-family: "Poppins", sans-serif;
    font-weight: 700;
    font-size: 68px;
    line-height: 86px;
    color: var(--sign-white);
    text-align: center;
    letter-spacing: 1px;
  }
  .sign__arrow {
    position: absolute;
    left: 0;
    top: 0;
    width: 513px;
    height: 413px;
  }
  .arrow-shape { fill: var(--arrow-orange); }
</style>
</head>
<body>
<main class="canvas">
  <section class="sign sign--left" aria-label="Office entrance sign, arrow pointing left">
    <header class="sign__header">
      <span class="brand-dot"></span>
      <span class="brand-name">skorNABEL</span>
    </header>
    <div class="sign__body">
      <p class="sign__label">Office<br>Entrance</p>
      <svg class="sign__arrow" viewBox="0 0 513 413" aria-hidden="true">
        <polygon class="arrow-shape" points="64,296 160,260 160,274 450,274 450,317 160,317 160,332"/>
      </svg>
    </div>
  </section>

  <section class="sign sign--right" aria-label="Office entrance sign, arrow pointing right">
    <header class="sign__header">
      <span class="brand-dot"></span>
      <span class="brand-name">skorNABEL</span>
    </header>
    <div class="sign__body">
      <p class="sign__label">Office<br>Entrance</p>
      <svg class="sign__arrow" viewBox="0 0 513 413" aria-hidden="true">
        <polygon class="arrow-shape" points="449,296 353,260 353,274 63,274 63,317 353,317 353,332"/>
      </svg>
    </div>
  </section>
</main>
</body>
</html>
```